Redesign Craft Brewing Recipe Website

Originally built with Bootstrap just to get the site going, I am seeking a complete redesign of the sites home page and recipe page. I am an experienced web developer with no graphic background, initially just looking for psd mocks.

I prefer styles that are clean and modern, and would prefer anything that is fun, engaging, and has an organic feel to it. I currently have a cartoon rabbit as a logo, but it needs some modification/tweaking, so any help in that area would be great as well.

Current site:
http://kettlewren.plumhostsite.net/

Current launch page/logo:
http://www.kettlewren.com/

I like the overall layout of the elements currently, but the design sucks.

The launch page is at the following URL

Reason: Still looking for a more modern design. Designs received so far are too similar to the original.

My site is content based and does not contain images or products. Your design should not consist of large images.

Reason: The website has very little images, so the designs need to be more text and content based. The header needs to be very small and should not contain an ad rotater.

Target Market(s)

Home brewers, Craft brewers, Microbreweries, Brewpubs

Requirements
Must have
• Web 2.0 Look and Feel, Fun, Hip, Focus on content
Should not have
• A large photo as a header

```html
<!DOCTYPE html>
<html lang="en">
<head>
<meta charset="utf-8">
<title>Kettlewren – create and share home brew</title>
<link rel="stylesheet" href="https://fonts.googleapis.com/css2?family=Noto+Sans:wght@400;700&family=Arimo:wght@400;700&display=swap">
<style>
:root{
  --launch-bg:#c8c8c8;
  --band-white:#ffffff;
  --brand-red:#b30000;
  --ink:#555555;
  --dark:#3a3a3a;
  --darker:#2a2a2a;
  --night:#161616;
  --site-bg:#d4d4d4;
  --panel:#efefef;
  --card:#f7f7f7;
  --sidebar:#ffffff;
  --link:#2a8ad0;
  --tab-blue:#1e88d0;
  --text:#333333;
  --muted:#999999;
  --tag-green:#3f8f3f;
  --tag-orange:#f0900a;
  --tag-grey:#9a9a9a;
  --srm-amber:#c08a3e;
  --srm-yellow:#e6e21a;
  --srm-black:#111111;
  --line:#dddddd;
}
*{box-sizing:border-box;margin:0;padding:0}
html,body{width:1015px;height:1200px;overflow:hidden}
body{position:relative;background:var(--launch-bg);font-family:"Arimo",Arial,sans-serif;color:var(--text)}
.abs{position:absolute}

/* launch page */
.launch-logo{left:400px;top:92px;width:215px;height:213px;background:var(--brand-red);display:flex;align-items:flex-end;justify-content:center;padding-bottom:52px}
.launch-logo span{font-family:"Noto Sans",sans-serif;color:#fff;font-size:32px;font-weight:400;letter-spacing:-0.5px}
.launch-band{left:0;top:313px;width:1015px;height:63px;background:var(--band-white);display:flex;align-items:center;justify-content:center}
.launch-band p{font-family:"Noto Sans",sans-serif;font-size:20px;color:var(--ink)}
.countdown{left:375px;top:390px;width:267px;height:93px;background:var(--dark);text-align:center;font-family:"Noto Sans",sans-serif;color:#fff}
.countdown .note{font-size:16px;line-height:21px;padding-top:4px}
.countdown .digits{position:absolute;left:9px;right:9px;top:61px;height:32px;background:var(--darker);display:flex;justify-content:center}
.countdown-labels{left:408px;top:483px;width:202px;height:27px;background:#fff;display:flex;font-family:"Noto Sans",sans-serif;font-size:16px;color:var(--text)}
.digits span,.countdown-labels span{width:50.5px;text-align:center}
.digits span{font-size:19px;line-height:32px}
.countdown-labels span{line-height:27px}
.digits{padding:0 33px}

.night-band{left:0;top:534px;width:1015px;height:57px;background:var(--night)}

/* site page */
.site{left:0;top:591px;width:1015px;height:576px;background:var(--site-bg);border-left:2px solid #eee}
.site-logo{left:124px;top:599px;width:64px;height:63px;background:var(--brand-red);display:flex;align-items:flex-end;justify-content:center;padding-bottom:12px}
.site-logo span{color:#fff;font-size:11px;font-family:"Noto Sans",sans-serif}
.site-tagline{left:109px;top:662px;width:216px;height:14px;background:var(--dark);color:#fff;font-size:9px;line-height:14px;padding-left:8px}
.top-nav{left:796px;top:662px;display:flex;gap:2px}
.top-nav span{background:#bdbdbd;color:var(--text);font-size:9px;line-height:14px;padding:0 6px}
.panel{left:109px;top:676px;width:781px;height:491px;background:var(--panel)}

.sidebar{left:124px;top:690px;width:163px;height:320px;background:var(--sidebar);padding:10px 6px;font-size:8.5px}
.search{display:flex;gap:3px;margin-bottom:10px}
.search .field{width:118px;height:21px;border:1px solid #ccc;color:#aaa;padding:4px 5px}
.search .go{width:32px;height:21px;border:1px solid #ccc;background:#f2f2f2;text-align:center;line-height:19px;color:#555}
.side-heading{font-size:7.5px;font-weight:700;color:#aaa;margin:8px 0 4px}
.opt{display:flex;align-items:center;gap:6px;height:17px;color:var(--text)}
.opt i{width:9px;height:9px;border:1px solid #4a6fb5;display:block}
.styles{position:relative;height:137px;overflow:hidden}
.scrollbar{position:absolute;right:0;top:0;width:11px;height:137px;background:#eef;border:1px solid #ccd}
.scrollbar b{position:absolute;left:1px;width:7px;height:10px;background:#a8bde8}
.scrollbar .thumb{top:16px;height:40px;background:#dde4f4}

.tabs{left:321px;top:690px;display:flex;gap:6px;font-size:8.5px}
.tabs span{padding:2px 7px;color:var(--link)}
.tabs .active{background:var(--tab-blue);color:#fff}

.card{width:270px;height:142px;background:var(--card);padding:10px 12px}
.card h3{font-size:11px;font-weight:400;color:var(--link);margin-bottom:6px}
.card p{font-size:8.5px;line-height:11px;color:var(--text)}
.card .by{font-size:7.5px;color:var(--muted);margin-top:6px}
.card .by a{color:var(--link);text-decoration:none}
.tags{display:flex;gap:5px;margin-top:8px}
.tag{font-size:7.5px;font-weight:700;color:#fff;padding:2px 5px;border-radius:2px}
.tag.extract{background:var(--tag-green)}
.tag.partial{background:var(--tag-orange)}
.tag.style{background:var(--tag-grey)}
.stats{position:absolute;right:0;bottom:0;display:flex;height:35px;background:#fff}
.stats div{width:41px;border-left:1px solid var(--line);text-align:center;font-size:8px;padding-top:6px;line-height:12px}
.stats .srm{border:none}
.srm.amber{background:var(--srm-amber)}
.srm.yellow{background:var(--srm-yellow)}
.srm.black{background:var(--srm-black);color:#111}

.footer{left:0;top:1167px;width:1015px;height:33px;background:var(--night);color:#ddd;font-size:9px;line-height:33px}
.footer .legal{position:absolute;left:124px}
.footer .links{position:absolute;right:142px;display:flex;gap:12px}
</style>
</head>
<body>

<!-- launch page -->
<div class="abs launch-logo"><span>Kettlewren</span></div>
<div class="abs launch-band"><p>The easiest way to create and share home brew</p></div>
<div class="abs countdown">
  <p class="note">Almost there, we are cleaning up<br>the mess and preparing to launch!</p>
  <div class="digits"><span>79</span><span>5</span><span>30</span><span>25</span></div>
</div>
<div class="abs countdown-labels"><span>Days</span><span>Hours</span><span>Min</span><span>Sec</span></div>

<div class="abs night-band"></div>

<!-- site home page -->
<div class="abs site"></div>
<div class="abs panel"></div>
<div class="abs site-logo"><span>Kettlewren</span></div>
<div class="abs site-tagline">The easiest way to create and share home brew</div>
<nav class="abs top-nav"><span>Recipes</span><span>Login</span></nav>

<aside class="abs sidebar">
  <div class="search"><div class="field">Stout</div><div class="go">GO</div></div>
  <h4 class="side-heading">BREWING</h4>
  <div class="opt"><i></i>Extract</div>
  <div class="opt"><i></i>Partial Mash</div>
  <div class="opt"><i></i>All Grain</div>
  <h4 class="side-heading">STYLES</h4>
  <div class="styles">
    <div class="opt"><i></i>American Amber Ale</div>
    <div class="opt"><i></i>American Barleywine</div>
    <div class="opt"><i></i>American Brown Ale</div>
    <div class="opt"><i></i>American IPA</div>
    <div class="opt"><i></i>American Pale Ale</div>
    <div class="opt"><i></i>American Stout</div>
    <div class="opt"><i></i>American Wheat or Rye Beer</div>
    <div class="opt"><i></i>Applewine</div>
    <div class="scrollbar"><b style="top:1px"></b><b class="thumb"></b><b style="bottom:1px"></b></div>
  </div>
  <h4 class="side-heading">MATCH MAKER</h4>
  <div class="opt"><i></i>Boil Size</div>
</aside>

<div class="abs tabs"><span class="active">Recent</span><span>Popular</span></div>

<article class="abs card" style="left:321px;top:716px">
  <h3>Honeysucker Belgian Tripel</h3>
  <p>Lorem ipsum dolor sit amet, consectetur adipisicing elit, sed do eiusmod tempor incididunt ut labore et dolore magna aliqua.</p>
  <p class="by">created by <a>Dale Hartwell</a></p>
  <div class="tags"><span class="tag extract">Extract</span><span class="tag style">Belgian Tripel</span></div>
  <div class="stats"><div>5.08%<br>abv</div><div>55<br>ibu</div><div>1.013<br>fg</div><div>1.051<br>og</div><div class="srm amber">9<br>srm</div></div>
</article>

<article class="abs card" style="left:608px;top:716px">
  <h3>Oak Hollow Sweet Mead</h3>
  <p>Lorem ipsum dolor sit amet, consectetur adipisicing elit, sed do eiusmod tempor incididunt ut labore et dolore magna aliqua.</p>
  <p class="by">created by <a>Dale Hartwell</a></p>
  <div class="tags"><span class="tag extract">Extract</span><span class="tag style">Sweet Mead</span></div>
  <div class="stats"><div>2.24%<br>abv</div><div>24<br>ibu</div><div>1.006<br>fg</div><div>1.022<br>og</div><div class="srm yellow">4<br>srm</div></div>
</article>

<article class="abs card" style="left:321px;top:868px">
  <h3>Venom Belgian Specialty Ale</h3>
  <p>Lorem ipsum dolor sit amet, consectetur adipisicing elit, sed do eiusmod tempor incididunt ut labore et dolore magna aliqua.</p>
  <p class="by">created by <a>Dale Hartwell</a></p>
  <div class="tags"><span class="tag partial">PartialMash</span><span class="tag style">Belgian Specialty Ale</span></div>
  <div class="stats"><div>13.93%<br>abv</div><div>126<br>ibu</div><div>1.036<br>fg</div><div>1.139<br>og</div><div class="srm black">40<br>srm</div></div>
</article>

<article class="abs card" style="left:608px;top:868px">
  <h3>Venom Mild</h3>
  <p>Lorem ipsum dolor sit amet, consectetur adipisicing elit, sed do eiusmod tempor incididunt ut labore et dolore magna aliqua.</p>
  <p class="by">created by <a>Dale Hartwell</a></p>
  <div class="tags"><span class="tag partial">PartialMash</span><span class="tag style">Mild</span></div>
  <div class="stats"><div>5.08%<br>abv</div><div>55<br>ibu</div><div>1.013<br>fg</div><div>1.051<br>og</div><div class="srm amber">9<br>srm</div></div>
</article>

<article class="abs card" style="left:321px;top:1020px">
  <h3>Lantern Hill Sweet Stout</h3>
  <p>Lorem ipsum dolor sit amet, consectetur adipisicing elit, sed do eiusmod tempor incididunt ut labore et dolore magna aliqua.</p>
  <p class="by">created by <a>Dale Hartwell</a></p>
  <div class="tags"><span class="tag extract">Extract</span><span class="tag style">Sweet Stout</span></div>
  <div class="stats"><div>2.24%<br>abv</div><div>24<br>ibu</div><div>1.006<br>fg</div><div>1.022<br>og</div><div class="srm yellow">4<br>srm</div></div>
</article>

<article class="abs card" style="left:608px;top:1020px">
  <h3>Capitol Dunkelweizen</h3>
  <p>Lorem ipsum dolor sit amet, consectetur adipisicing elit, sed do eiusmod tempor incididunt ut labore et dolore magna aliqua.</p>
  <p class="by">created by <a>Dale Hartwell</a></p>
  <div class="tags"><span class="tag extract">Extract</span><span class="tag style">Dunkelweizen</span></div>
  <div class="stats"><div>13.93%<br>abv</div><div>126<br>ibu</div><div>1.036<br>fg</div><div>1.139<br>og</div><div class="srm black">40<br>srm</div></div>
</article>

<footer class="abs footer">
  <span class="legal">© Kettlewren, Inc. All third party content © their respective owners.</span>
  <span class="links"><span>Terms of Service</span><span>Contact</span></span>
</footer>

</body>
</html>
```